Plate Parade! Digital Order Web App

This is a web app on mobile phone, for consumers to order food inside a restaurant using their phones. we have done up the flow but we need to revamp UI design. pls have a look at our current web on your mobile phone:
https://demo.pesanly.app/o/KWLM/274615

CURRENT DESIGN.
1. food category on left side, always shown. menu items in list view with image.
2. when we click on an item, there is popup page, to select modifiers, or quantity.
3. order review page(cart page) is quite messy now, need a complete new look.
4 payment page(no need to design, handle by Paxtel)
5. order confirmation page. success or error return

DESIGN requirements:
please browse through and click to order with current page above. we have put in lots of thoughts and effort for current flow, the new design should base on this flow.
1. web app. no zoom in/out is allowed for users. responsive html to suit different mobile phone screen size. modern fonts.
2. PAGES needed:
home/welcome page,
well laid out menu items page,
single item page, with add on choice and modifier
cart page(to include recommended items, ordered item list, remove item total, changeable quantity,
confirmation page(success, fail)

DELIVERABLES - responsive html, fonts, images asset such as icons, animation, button images(suitable for commercial use without further third party loyalty fee)

Hi all if we have left a comment on ur design, please revise accordingly and we will conclude it soon!

Target Market(s)

young diners who order food on their mobile phone.

Industry/Entity Type

Restaurant

Coding

Coded - Design and coding required

Number of Pages Required

5+ page

Colors

Designer to choose colors to be used in the design.

Requirements
Must have
• - lively, appetising colors while making the page easy to read. easy on eyes.
• - consistency. fonts used.
Nice to have
• - 2 color schemes
• - html codes. we will top up if you can deliver coded html.
Should not have
• - should not have more than 3 colors
• - should not have more than 3 different fonts
• - should not use colors that are dull

```html
<!DOCTYPE html>
<html lang="en">
<head>
<meta charset="utf-8">
<title>Pesanly – Order Screens</title>
<link rel="stylesheet" href="https://fonts.googleapis.com/css2?family=Lato:wght@400;700;900&display=swap">
<style>
:root{
  --orange:#ff5a0a;
  --orange-deep:#a9420f;
  --ink:#24292d;
  --line:#4a4f53;
  --white:#ffffff;
  --page:#f3f3f3;
  --food-a:#c98a2a;
  --food-b:#6b4424;
  --plate-a:#f4efe9;
  --plate-b:#c9a48a;
}
*{box-sizing:border-box;margin:0;padding:0}
html,body{width:1200px;height:1125px;overflow:hidden}
body{background:var(--page);font-family:"Lato",sans-serif;color:var(--white);position:relative}
.screen{position:absolute;top:40px;width:265px;background:var(--ink);overflow:hidden;border-radius:28px}
.screen--menu{left:90px;height:560px}
.screen--item{left:467px;height:560px}
.screen--cart{left:845px;height:1045px}

/* header */
.app-bar{position:relative;height:140px;background:var(--orange);border-radius:0 0 50% 50% / 0 0 22px 22px}
.brand{position:absolute;top:38px;left:0;right:0;text-align:center;font-weight:700;font-size:22px}
.login{position:absolute;top:43px;right:16px;font-size:12px;display:flex;align-items:center;gap:5px}
.tool-row{position:absolute;top:80px;left:12px;right:12px;display:flex;align-items:center;justify-content:space-between}
.search{display:flex;width:150px;height:22px;background:var(--white);border:2px solid var(--white);border-radius:2px}
.search span{flex:1;color:var(--orange);font-size:8px;padding:5px 6px}
.search i{width:38px;background:var(--orange);display:flex;align-items:center;justify-content:center}

/* menu */
.menu-body{position:absolute;top:150px;left:0;right:0;bottom:0;display:flex}
.categories{width:90px;list-style:none;background:var(--orange-deep);align-self:flex-start}
.categories li{font-size:10px;padding:6px 8px;height:27px;border-bottom:1px solid #c56a3a;margin:0 3px}
.categories li.is-active{color:#e0a07c}
.dishes{flex:1;padding:0 10px 0 6px}
.dishes h2{font-size:15px;font-weight:700;text-align:center;margin:10px 0 8px}
.dish{display:flex;align-items:flex-start;gap:6px;height:62px;position:relative}
.dish-photo{width:63px;height:40px;background:linear-gradient(135deg,var(--food-a),var(--food-b));border:1px solid #ddd}
.dish-photo.green{background:linear-gradient(135deg,#5d8a2c,#2f4d18)}
.dish-name{font-size:7px;font-weight:700;margin-top:1px}
.dish-price{font-size:8px;font-weight:700;margin-top:6px}
.add{position:absolute;right:0;top:30px;width:11px;height:11px;border-radius:50%;background:var(--orange);font-size:10px;line-height:11px;text-align:center;font-weight:900}

/* popup */
.dim{position:absolute;top:140px;left:0;right:0;bottom:0;background:rgba(150,150,150,.55)}
.popup{position:absolute;top:206px;left:14px;right:14px}
.popup-photo{height:100px;background:linear-gradient(135deg,#f0b63a,#b86d1c)}
.popup-panel{background:var(--orange);padding:14px 12px 12px}
.popup-panel h3{font-size:11px;font-weight:400;text-align:center}
.popup-row{display:flex;justify-content:space-between;align-items:center;margin-top:16px;font-size:9px;font-weight:700}
.qty{display:flex;border:1.5px solid var(--white);height:15px;font-size:9px;align-items:center}
.qty b{width:14px;text-align:center}
.qty span{width:14px;text-align:center;background:var(--white);color:var(--orange);height:100%;line-height:13px}
.popup-actions{display:flex;justify-content:space-between;margin-top:12px}
.ghost{background:var(--white);color:var(--orange);border:1.5px solid var(--white);font-size:9px;padding:3px 0;width:92px;text-align:center}

/* cart */
.cart-body{position:absolute;top:140px;left:0;right:0}
.tab{display:inline-block;background:var(--orange);font-size:10.5px;font-weight:700;padding:8px 34px 8px 16px;clip-path:polygon(0 0,100% 0,92% 100%,0 100%);margin-top:12px}
.order-list{list-style:none;margin:14px 12px 0}
.order-list li{display:flex;align-items:center;height:50px;border-bottom:1px solid var(--line);font-size:7.5px;font-weight:700}
.order-list .qty{margin-right:12px;border-color:var(--white)}
.order-list .qty b{background:var(--orange)}
.order-list .price{margin-left:auto;font-size:10px;font-weight:400}
.recs{display:flex;gap:14px;margin:16px 0 0 15px}
.rec{width:102px;height:58px;background:linear-gradient(135deg,var(--plate-a),var(--plate-b));border:2px solid var(--white)}
.label{font-size:10.5px;margin:30px 0 0 16px}
.field{height:27px;background:var(--white);margin:16px 13px 0;border-radius:1px}
.sums{margin-top:18px}
.sum{display:flex;align-items:center;margin:0 12px;font-size:10px;height:32px}
.sum i{flex:1;border-top:1px dashed #999;margin:0 12px}
.remove{display:block;width:175px;margin:12px auto 14px;background:var(--orange);text-align:center;font-size:10px;padding:9px 0}
.hint{font-size:10px;margin:20px 0 0 16px}
.pay{display:block;margin:18px 14px 0;border:2px solid var(--orange);outline:2px solid var(--white);outline-offset:-4px;background:var(--white);color:var(--orange);text-align:center;font-size:9px;font-weight:700;padding:8px 0}
.pay + .pay{margin-top:12px}
</style>
</head>
<body>

<!-- Menu screen -->
<section class="screen screen--menu">
  <header class="app-bar">
    <div class="brand">Pesanly</div>
    <div class="login">login <svg width="13" height="12" viewBox="0 0 13 12" fill="none" stroke="#fff" stroke-width="1.6"><path d="M1 6h7M5 3l3 3-3 3M9 1h3v10H9"/></svg></div>
    <div class="tool-row">
      <svg width="20" height="16" viewBox="0 0 20 16"><rect y="1" width="20" height="3" fill="#fff"/><rect y="7" width="20" height="3" fill="#fff"/><rect y="13" width="20" height="3" fill="#fff"/></svg>
      <div class="search"><span>Search</span><i><svg width="12" height="12" viewBox="0 0 12 12" fill="none" stroke="#fff" stroke-width="1.5"><circle cx="5" cy="5" r="3.5"/><path d="M7.5 7.5L11 11"/></svg></i></div>
      <svg width="24" height="20" viewBox="0 0 24 20" fill="none" stroke="#fff" stroke-width="1.6"><path d="M1 3h4l3 11h12l3-9H7M9 6v6M13 6v6M17 6v6"/><circle cx="10" cy="17.5" r="1.5"/><circle cx="18" cy="17.5" r="1.5"/></svg>
    </div>
  </header>
  <div class="menu-body">
    <ul class="categories">
      <li class="is-active">Vegetable</li><li>Meat</li><li>Seafood</li><li>Special</li><li>Cold Dish</li><li>Main</li><li>Set</li><li>Juice</li><li>Meals</li><li>Vegetarian</li>
    </ul>
    <div class="dishes">
      <h2>Vegetable</h2>
      <div class="dish"><div class="dish-photo" role="img" aria-label="Grilled skewers photo"></div><div><p class="dish-name">Lorem ipsum dolor sit</p><p class="dish-price">$15.20</p></div><span class="add">+</span></div>
      <div class="dish"><div class="dish-photo" role="img" aria-label="Grilled oyster photo"></div><div><p class="dish-name">Grilled Oyster</p><p class="dish-price">$15.20</p></div><span class="add">+</span></div>
      <div class="dish"><div class="dish-photo" role="img" aria-label="Grilled pleurotus photo"></div><div><p class="dish-name">Grilled Pleurotus</p><p class="dish-price">$15.20</p></div><span class="add">+</span></div>
      <div class="dish"><div class="dish-photo green" role="img" aria-label="Grilled string bean photo"></div><div><p class="dish-name">Grilled String Bean</p><p class="dish-price">$15.20</p></div><span class="add">+</span></div>
      <div class="dish"><div class="dish-photo" role="img" aria-label="Grilled sweet corn photo"></div><div><p class="dish-name">Grilled Sweet Corn</p><p class="dish-price">$15.20</p></div><span class="add">+</span></div>
      <div class="dish"><div class="dish-photo" role="img" aria-label="Grilled potato chip photo"></div><div><p class="dish-name">Grilled Potato Chip</p><p class="dish-price">$15.20</p></div><span class="add">+</span></div>
    </div>
  </div>
</section>

<!-- Item popup screen -->
<section class="screen screen--item">
  <header class="app-bar">
    <div class="brand">Pesanly</div>
    <div class="login">login <svg width="13" height="12" viewBox="0 0 13 12" fill="none" stroke="#fff" stroke-width="1.6"><path d="M1 6h7M5 3l3 3-3 3M9 1h3v10H9"/></svg></div>
    <div class="tool-row">
      <svg width="20" height="16" viewBox="0 0 20 16"><rect y="1" width="20" height="3" fill="#fff"/><rect y="7" width="20" height="3" fill="#fff"/><rect y="13" width="20" height="3" fill="#fff"/></svg>
      <div class="search"><span>Search</span><i><svg width="12" height="12" viewBox="0 0 12 12" fill="none" stroke="#fff" stroke-width="1.5"><circle cx="5" cy="5" r="3.5"/><path d="M7.5 7.5L11 11"/></svg></i></div>
      <svg width="24" height="20" viewBox="0 0 24 20" fill="none" stroke="#fff" stroke-width="1.6"><path d="M1 3h4l3 11h12l3-9H7M9 6v6M13 6v6M17 6v6"/><circle cx="10" cy="17.5" r="1.5"/><circle cx="18" cy="17.5" r="1.5"/></svg>
    </div>
  </header>
  <div class="menu-body">
    <ul class="categories">
      <li class="is-active">Vegetable</li><li>Meat</li>
    </ul>
    <div class="dishes">
      <h2>Vegetable</h2>
      <div class="dish"><div class="dish-photo" role="img" aria-label="Grilled skewers photo"></div><div><p class="dish-name">Lorem ipsum dolor sit</p><p class="dish-price">$15.20</p></div><span class="add">+</span></div>
      <div class="dish"></div><div class="dish"></div><div class="dish"></div>
      <div class="dish"><div class="dish-photo" role="img" aria-label="Grilled sweet corn photo"></div><div><p class="dish-name">Grilled Sweet Corn</p><p class="dish-price">$15.20</p></div><span class="add">+</span></div>
      <div class="dish"><div class="dish-photo" role="img" aria-label="Grilled potato chip photo"></div><div><p class="dish-name">Grilled Potato Chip</p><p class="dish-price">$15.20</p></div><span class="add">+</span></div>
    </div>
  </div>
  <div class="dim"></div>
  <div class="popup">
    <div class="popup-photo" role="img" aria-label="Grilled king oyster mushroom photo"></div>
    <div class="popup-panel">
      <h3>Grilled Pleurotus Eryngii</h3>
      <div class="popup-row"><span>$1.50</span><div class="qty"><b>+</b><span>1</span><b>−</b></div></div>
      <div class="popup-actions"><span class="ghost">Remarks</span><span class="ghost">Add to cart</span></div>
    </div>
  </div>
</section>

<!-- Cart screen -->
<section class="screen screen--cart">
  <header class="app-bar">
    <div class="brand">Pesanly</div>
    <div class="login">login <svg width="13" height="12" viewBox="0 0 13 12" fill="none" stroke="#fff" stroke-width="1.6"><path d="M1 6h7M5 3l3 3-3 3M9 1h3v10H9"/></svg></div>
    <div class="tool-row">
      <svg width="20" height="16" viewBox="0 0 20 16"><rect y="1" width="20" height="3" fill="#fff"/><rect y="7" width="20" height="3" fill="#fff"/><rect y="13" width="20" height="3" fill="#fff"/></svg>
      <div class="search"><span>Search</span><i><svg width="12" height="12" viewBox="0 0 12 12" fill="none" stroke="#fff" stroke-width="1.5"><circle cx="5" cy="5" r="3.5"/><path d="M7.5 7.5L11 11"/></svg></i></div>
      <svg width="24" height="20" viewBox="0 0 24 20" fill="none" stroke="#fff" stroke-width="1.6"><path d="M1 3h4l3 11h12l3-9H7M9 6v6M13 6v6M17 6v6"/><circle cx="10" cy="17.5" r="1.5"/><circle cx="18" cy="17.5" r="1.5"/></svg>
    </div>
  </header>
  <div class="cart-body">
    <div class="tab">Review Your Order</div>
    <ul class="order-list">
      <li><div class="qty"><b>+</b><span>1</span><b>−</b></div>Grilled Pleurotus Eryngii<span class="price">$15.00</span></li>
      <li><div class="qty"><b>+</b><span>1</span><b>−</b></div>Grilled String Bean<span class="price">$13.00</span></li>
      <li><div class="qty"><b>+</b><span>1</span><b>−</b></div>Grilled String Bean<span class="price">$13.00</span></li>
    </ul>
    <div class="tab" style="margin-top:10px">Recommended items</div>
    <div class="recs">
      <div class="rec" role="img" aria-label="Recommended set meal photo"></div>
      <div class="rec" role="img" aria-label="Recommended set meal photo"></div>
    </div>
    <p class="label">Remarks For all items</p>
    <div class="field"></div>
    <div class="sums">
      <div class="sum"><span>Subtotal</span><i></i><span>$13.00</span></div>
      <div class="sum"><span>Total</span><i></i><span>$15.00</span></div>
    </div>
    <span class="remove">REMOVE ALL ITEM</span>
    <div class="tab">2.Key in Mobile No:</div>
    <p class="hint">To enjoy member benefits</p>
    <div class="field" style="margin-top:10px"></div>
    <div class="tab" style="margin-top:22px">3.Select a Payment:</div>
    <span class="pay">PAY WITH CREDIT CARD</span>
    <span class="pay">ADD OTHER ITEMS</span>
  </div>
</section>

</body>
</html>
```